Book Cover

Book cover for a study guide on Galatians. The title would be: "Unbound Hearts: Called Out to Walk Open" Possibly using a bird breaking free from a cage.+

Target Market(s)

We will sell them to our church.

Requirements
Must have
• Authors are Dr. Martin Oskerby and Dr. Helen Oskerby

```html
<!DOCTYPE html>
<html lang="en">
<head>
<meta charset="utf-8">
<title>Unbound Hearts: Called Out to Walk Open</title>
<link rel="stylesheet" href="https://fonts.googleapis.com/css2?family=Michroma&family=Barlow+Semi+Condensed:wght@700&family=Courier+Prime:wght@700&display=swap">
<style>
  :root {
    --page: #ffffff;
    --sky-light: #cfe6f2;
    --sky-mid: #a9d3ea;
    --wash-yellow: #e6edc0;
    --wash-gold: #d9b978;
    --bird-blue: #4d6a93;
    --bird-deep: #273f6e;
    --gold-light: #f2b43c;
    --gold: #e59f22;
    --gold-deep: #c9821a;
    --navy: #1c2a5a;
    --rust: #a9642a;
    --label-bg: #ffffff;
  }
  * { margin: 0; padding: 0; box-sizing: border-box; }
  html, body {
    width: 1200px; height: 1200px; overflow: hidden;
    background: var(--page);
  }
  .canvas { position: relative; width: 1200px; height: 1200px; }
  .cover {
    position: absolute; left: 240px; top: 60px;
    width: 720px; height: 1080px; overflow: hidden;
  }
  .cover-art { position: absolute; inset: 0; width: 100%; height: 100%; }
  .cross-title {
    position: absolute; left: 89px; top: 140px;
    width: 162px; height: 940px;
    display: flex; flex-direction: column; align-items: center; justify-content: flex-start;
    font-family: "Michroma", sans-serif; font-size: 50px; line-height: 64px;
    color: var(--navy);
  }
  .cross-title .word { display: flex; flex-direction: column; align-items: center; }
  .cross-title .word + .word { margin-top: 26px; }
  .subtitle-label {
    position: absolute; left: 339px; top: 222px;
    width: 381px; height: 159px;
    background: var(--label-bg);
    box-shadow: 0 2px 4px rgba(0,0,0,0.18);
    padding: 30px 20px 0 16px;
  }
  .subtitle {
    font-family: "Barlow Semi Condensed", sans-serif; font-weight: 700;
    font-size: 31px; color: var(--navy); white-space: nowrap; text-align: center;
  }
  .authors {
    margin-top: 24px; text-align: right;
    font-family: "Courier Prime", monospace; font-weight: 700;
    font-size: 15px; line-height: 22px; color: var(--rust);
  }
</style>
</head>
<body>
<main class="canvas">
  <article class="cover">
    <svg class="cover-art" viewBox="0 0 720 1080" xmlns="http://www.w3.org/2000/svg">
      <defs>
        <linearGradient id="skyWash" x1="0" y1="0" x2="0.3" y2="1">
          <stop offset="0" stop-color="var(--sky-light)"/>
          <stop offset="0.35" stop-color="var(--sky-mid)"/>
          <stop offset="0.6" stop-color="var(--wash-yellow)"/>
          <stop offset="0.85" stop-color="var(--bird-blue)"/>
          <stop offset="1" stop-color="var(--bird-deep)"/>
        </linearGradient>
        <radialGradient id="goldWash" cx="0.75" cy="0.08" r="0.35">
          <stop offset="0" stop-color="var(--wash-gold)" stop-opacity="0.85"/>
          <stop offset="1" stop-color="var(--wash-gold)" stop-opacity="0"/>
        </radialGradient>
        <linearGradient id="goldLeaf" x1="0" y1="0" x2="1" y2="1">
          <stop offset="0" stop-color="var(--gold-light)"/>
          <stop offset="0.5" stop-color="var(--gold)"/>
          <stop offset="1" stop-color="var(--gold-deep)"/>
        </linearGradient>
      </defs>
      <g role="img" aria-label="Flock of pigeons taking flight across a pale blue sky with gold watercolour wash">
        <rect width="720" height="1080" fill="url(#skyWash)"/>
        <rect width="720" height="1080" fill="url(#goldWash)"/>
      </g>
      <g class="cross">
        <rect x="89" y="0" width="162" height="1080" fill="url(#goldLeaf)"/>
        <rect x="0" y="222" width="339" height="159" fill="url(#goldLeaf)"/>
      </g>
    </svg>
    <h1 class="cross-title" aria-label="Unbound Hearts">
      <span class="word"><span>U</span><span>N</span><span>B</span><span>O</span><span>U</span><span>N</span><span>D</span></span>
      <span class="word"><span>H</span><span>E</span><span>A</span><span>R</span><span>T</span><span>S</span></span>
    </h1>
    <div class="subtitle-label">
      <p class="subtitle">Called Out to Walk Open</p>
      <p class="authors">Dr. Martin Oskerby<br>Dr. Helen Oskerby</p>
    </div>
  </article>
</main>
</body>
</html>
```